Rack Flyer for Willowcrest Dementia

We need a rack flyer design providing information on services we offer, fees and relevant contact information. Using company branding (logo, font and colours). Must be provided in a format that is easily edited for ongoing use.

For DL size (99 x 210mm)

```html
<!DOCTYPE html>
<html lang="en">
<head>
<meta charset="utf-8">
<title>Willowcrest Dementia – DL Rack Flyer</title>
<link href="https://fonts.googleapis.com/css2?family=Montserrat:wght@500;600;700&family=Nunito+Sans:ital,wght@0,400;0,600;0,700;1,400&family=Yellowtail&display=swap" rel="stylesheet">
<style>
  :root{
    --navy:#24215a;
    --navy-deep:#201d54;
    --orange:#f5a524;
    --ink:#2a2760;
    --white:#ffffff;
    --stage:#dcdcdc;
  }
  *{margin:0;padding:0;box-sizing:border-box}
  html,body{width:1119px;height:1200px;overflow:hidden}
  body{background:var(--stage);position:relative;font-family:"Nunito Sans",sans-serif}

  .panel{position:absolute;top:186px;width:398px;height:843px;overflow:hidden}
  .panel--front{left:149px;background:var(--white)}
  .panel--back{left:567px;background:var(--navy)}

  /* front */
  .hero-photo{position:absolute;left:0;top:0;width:398px;height:262px;
    background:linear-gradient(160deg,#4f6b3a 0%,#8c8a80 35%,#c9a896 60%,#7d8591 100%)}
  .hero-wave{position:absolute;left:0;top:170px;width:398px;height:100px}
  .brand{position:absolute;left:44px;top:272px;display:flex;align-items:center;gap:10px}
  .brand__dot{width:26px;height:26px;border-radius:50%;background:var(--orange)}
  .brand__name{font-family:"Montserrat",sans-serif;font-weight:700;font-size:21px;color:var(--navy)}
  .headline{position:absolute;left:46px;top:346px;font-family:"Montserrat",sans-serif;font-weight:700;
    font-size:33px;line-height:42px;color:var(--navy);letter-spacing:.3px}
  .headline__script{position:absolute;left:36px;top:400px;font-family:"Yellowtail",cursive;font-size:86px;
    color:var(--orange);line-height:1}
  .intro{position:absolute;left:42px;width:312px;font-size:10.6px;line-height:13.7px;color:var(--ink)}
  .intro--lead{top:520px}
  .intro--body{top:591px}
  .contact-list{position:absolute;left:38px;top:733px;list-style:none}
  .contact-list li{display:flex;align-items:center;gap:7px;height:28px;font-size:15px;color:var(--ink)}
  .contact-icon{width:20px;height:20px;border-radius:50%;background:var(--orange);display:flex;align-items:center;justify-content:center}

  /* back */
  .script-title{position:absolute;left:0;width:398px;text-align:center;font-family:"Yellowtail",cursive;
    color:var(--orange);font-size:52px;line-height:1}
  .script-title--services{top:30px}
  .script-title--fees{top:382px}
  .service-list{position:absolute;left:37px;top:104px;width:300px;list-style:none}
  .service-list li{position:relative;padding-left:20px;font-size:10.6px;line-height:12.5px;color:var(--white);margin-bottom:8.5px}
  .service-list li::before{content:"";position:absolute;left:0;top:1.5px;width:10px;height:10px;border-radius:50%;background:var(--orange)}
  .service-list li::after{content:"";position:absolute;left:3px;top:3.5px;width:3px;height:5px;border:solid var(--navy);border-width:0 1.5px 1.5px 0;transform:rotate(45deg)}
  .fee-table{position:absolute;left:36px;top:457px;width:304px;list-style:none}
  .fee-row{display:flex;align-items:flex-end;font-size:10.8px;line-height:13px;color:var(--white);margin-bottom:5px}
  .fee-row__label{white-space:nowrap}
  .fee-row__label--wrap{white-space:normal;width:238px}
  .fee-row__dots{flex:1;border-bottom:1px dotted rgba(255,255,255,.6);margin:0 6px 3px}
  .fee-row__price{color:var(--orange);font-weight:700;width:30px;text-align:right}
  .fee-term{text-align:right;color:var(--orange);font-weight:700;font-size:10px;margin-top:-7px}
  .coverage{position:absolute;left:40px;top:591px;width:320px;text-align:center;font-style:italic;
    font-size:10.6px;line-height:13.7px;color:var(--white)}
  .cta{position:absolute;left:40px;top:694px;width:319px;height:47px;border-radius:5px;background:var(--orange);
    box-shadow:0 4px 8px rgba(0,0,0,.3);display:flex;align-items:center;justify-content:center;text-align:center;
    font-family:"Montserrat",sans-serif;font-weight:700;font-size:17px;line-height:20px;color:var(--navy)}
  .back-contacts{position:absolute;left:0;top:756px;width:398px;text-align:center;font-family:"Montserrat",sans-serif;
    font-weight:700;font-size:15.5px;line-height:22px;color:var(--white)}
  .back-contacts .accent{color:var(--orange)}
</style>
</head>
<body>

<section class="panel panel--front">
  <div class="hero-photo" role="img" aria-label="Photograph of a carer's hands gently holding an elderly person's hands"></div>
  <svg class="hero-wave" viewBox="0 0 398 100" preserveAspectRatio="none" aria-hidden="true">
    <path d="M0 60 C80 -5 170 5 260 40 C320 62 370 60 398 50 L398 100 L0 100 Z" fill="#f5a524"/>
    <path d="M0 82 C80 20 170 22 260 56 C320 78 370 86 398 82 L398 100 L0 100 Z" fill="#ffffff"/>
  </svg>

  <div class="brand">
    <span class="brand__dot"></span>
    <span class="brand__name">Willowcrest Dementia</span>
  </div>

  <h1 class="headline">NAVIGATING<br>DEMENTIA</h1>
  <div class="headline__script">together</div>

  <p class="intro intro--lead">Navigating a diagnosis of dementia can be daunting. You likely have many questions, and it can be overwhelming trying to figure out where to turn to for answers and help. We want you to know that you are not alone in this journey.</p>
  <p class="intro intro--body">As the numbers of those living with dementia in Bermuda continue to rise placing greater demands on an already strained health care system, Willowcrest's clinical and evidence based consultation services improve the safety, independence and quality of life of persons with dementia and their caregivers. Our goal is to assist clients to successfully age in place at home with the support of their family caregivers to reduce the overall cost and burden of care for this vulnerable population.</p>

  <ul class="contact-list">
    <li><span class="contact-icon"><svg width="12" height="12" viewBox="0 0 24 24"><path fill="#24215a" d="M6.6 10.8a15 15 0 0 0 6.6 6.6l2.2-2.2c.3-.3.7-.4 1-.2 1.1.4 2.3.6 3.6.6.6 0 1 .4 1 1V20c0 .6-.4 1-1 1A17 17 0 0 1 3 4c0-.6.4-1 1-1h3.5c.6 0 1 .4 1 1 0 1.3.2 2.5.6 3.6.1.3 0 .7-.2 1z"/></svg></span>(441) 555 0142</li>
    <li><span class="contact-icon"><svg width="12" height="12" viewBox="0 0 24 24" fill="none" stroke="#24215a" stroke-width="2"><circle cx="12" cy="12" r="9"/><path d="M3 12h18M12 3c3 3 3 15 0 18M12 3c-3 3-3 15 0 18"/></svg></span>www.willowcrestdementia.bm</li>
    <li><span class="contact-icon"><svg width="12" height="12" viewBox="0 0 24 24" fill="none" stroke="#24215a" stroke-width="2"><rect x="3" y="5" width="18" height="14"/><path d="M3 6l9 7 9-7"/></svg></span>info@willowcrestdementia.bm</li>
  </ul>
</section>

<section class="panel panel--back">
  <h2 class="script-title script-title--services">Services Offered</h2>
  <ul class="service-list">
    <li>Comprehensive Dementia Assessment</li>
    <li>Cognitive/Perceptual Screening</li>
    <li>Home Safety Audit (Home modifications and adaptive equipment aids)</li>
    <li>Caregiver Education &amp; Support</li>
    <li>Falls Prevention Strategies</li>
    <li>Personalised Care Planning</li>
    <li>Preparation for future disease progression</li>
    <li>Case Management Support</li>
    <li>Check-in/monitoring visits for clients with limited social support</li>
    <li>Cognitive Stimulation Therapy (group program for individuals with mild-moderate stage dementia)</li>
  </ul>

  <h2 class="script-title script-title--fees">Service Fees</h2>
  <ul class="fee-table">
    <li class="fee-row"><span class="fee-row__label">Initial Consultation</span><span class="fee-row__dots"></span><span class="fee-row__price">$180</span></li>
    <li class="fee-row"><span class="fee-row__label">Comprehensive Dementia Assessment</span><span class="fee-row__dots"></span><span class="fee-row__price">$395</span></li>
    <li class="fee-row"><span class="fee-row__label fee-row__label--wrap">Comprehensive Dementia Assessment &amp; ongoing case management services</span><span class="fee-row__dots"></span><span class="fee-row__price">$720</span></li>
    <li class="fee-row"><span class="fee-row__label">Monthly check in/monitoring visits</span><span class="fee-row__dots"></span><span class="fee-row__price">$180</span></li>
    <li class="fee-row"><span class="fee-row__label">Cognitive Stimulation Therapy</span><span class="fee-row__dots"></span><span class="fee-row__price">$500</span></li>
    <li class="fee-term">per term</li>
  </ul>

  <p class="coverage">We are pleased to share that services offered by Willowcrest Dementia are currently covered under Harbourline and Coralpoint health insurance plans. We also have availability of funding support for those in financial need who are unable to afford co-pay, enabling equitable access to these essential care and support services regardless of financial means.</p>

  <div class="cta">Please feel free to reach out<br>for further information.</div>

  <div class="back-contacts">
    <div>www.willowcrestdementia.bm</div>
    <div class="accent">info@willowcrestdementia.bm</div>
    <div>(441) 555 0142</div>
  </div>
</section>

</body>
</html>
```